Takeaway coffee cup design for a trending coffee shop in soho London

We need a background design similar to the image attached "image 1". with BRUMLA PEWTIN written as our logo in Veneer. attached also is our current cup "image 2" if it helps to capture our use of colours.
Hex Codes: YELLOW: #FFF0AD (BRUMLA Colour)
Green: #1E3226 (Back ground colour)
Orange: #FF803D (S & H Colour)

```html
<!DOCTYPE html>
<html lang="en">
<head>
<meta charset="utf-8">
<title>BRUMLA PEWTIN – Takeaway Cup Wrap</title>
<link rel="stylesheet" href="https://fonts.googleapis.com/css2?family=Bebas+Neue&display=swap">
<style>
  :root {
    --page-bg: #ffffff;
    --cup-green: #1e3226;
    --pattern-deep: #2b4034;
    --pattern-soft: #4d6356;
    --brand-yellow: #fff0ad;
    --brand-orange: #ff803d;
  }
  html, body {
    margin: 0;
    padding: 0;
    width: 1029px;
    height: 1200px;
    overflow: hidden;
    background: var(--page-bg);
  }
  .canvas {
    position: relative;
    width: 1029px;
    height: 1200px;
    background: var(--page-bg);
  }
  .cup-wrap {
    position: absolute;
    left: 70px;
    top: 410px;
    width: 914px;
    height: 379px;
    background: var(--cup-green);
    overflow: hidden;
  }
  .floral-band {
    position: absolute;
    left: 0;
    top: 77px;
    width: 100%;
    height: 225px;
    background: linear-gradient(90deg, var(--pattern-deep), var(--pattern-soft) 25%, var(--pattern-deep) 50%, var(--pattern-soft) 75%, var(--pattern-deep));
  }
  .wordmark {
    position: absolute;
    top: 140px;
    width: 240px;
    margin-left: -120px;
    font-family: "Bebas Neue", "Oswald", sans-serif;
    font-weight: 400;
    color: var(--brand-yellow);
    line-height: 1;
    text-align: center;
    white-space: nowrap;
  }
  .wordmark--left { left: 215px; }
  .wordmark--right { left: 657px; }
  .wordmark__name {
    display: block;
    font-size: 68px;
    letter-spacing: 1px;
  }
  .wordmark__place {
    position: relative;
    display: inline-block;
    margin-top: 4px;
    font-size: 36px;
    letter-spacing: 1px;
  }
  .wordmark__mark {
    position: absolute;
    left: -20px;
    top: 50%;
    width: 9px;
    height: 9px;
    margin-top: -6px;
    background: var(--brand-orange);
  }
</style>
</head>
<body>
  <main class="canvas">
    <section class="cup-wrap" aria-label="Takeaway cup wrap artwork">
      <div class="floral-band" role="img" aria-label="Band of soft grey-green botanical pattern with leaves, vines and small flowers"></div>

      <div class="wordmark wordmark--left">
        <span class="wordmark__name">BRUMLA</span>
        <span class="wordmark__place"><span class="wordmark__mark"></span>PEWTIN</span>
      </div>

      <div class="wordmark wordmark--right">
        <span class="wordmark__name">BRUMLA</span>
        <span class="wordmark__place"><span class="wordmark__mark"></span>PEWTIN</span>
      </div>
    </section>
  </main>
</body>
</html>
```